Quellmont Home Roadmap for Street Safety

We need to re-work our "Home Roadmap for Street Safety" brochures (English & Spanish) to give it greater visual appeal with updated photos and graphics; the content (text) is currently being edited, but is not expected to be drastically different. It's important that we uses images and graphics that strike a delicate balance between conveying the image of gangs or gang members without glorifying gangs or portraying the City or even a particular race in bad light. Abstract, silhouette, faceless, and ambiguous images are preferred. Other images portraying kids or families should be diverse (white, African-American, Latino, Asian, etc.) and inclusive of both males and females. The design should communicate that help and resources are available. Please see attachments for current brochure designs in Spanish and English.

Target Market(s)

Parents of gang members, gang-associates, and other at-risk youth

Industry/Entity Type

Work

Font styles to use
Serif

Requirements
Must have
• City of Quellmont logo. We''re flexible on the size... could be 8.5" x 14" folded to a 4-panel, 2-sided brochure, or could simply be 8.5'' x 11" folded in half. The current brochure design can give you an idea of the space required for the content.
Nice to have
• Some images that might covey the idea of police interaction such as a silhouette or no-face image from behind gang members or police officers and police cars in dark alley. Also, positive images of Oxnard scenes or families and non-gang kids (boys & girls) of various ethnicities (white, African-American, Latino, Asian) .
Should not have
• Images that may be perceived negatively such as bloody crime scenes, officers using guns, batons, or handcuffs, or images that glorify the gang lifestyle

```html
<!DOCTYPE html>
<html lang="en">
<head>
<meta charset="utf-8">
<title>Quellmont Home Roadmap for Street Safety</title>
<link href="https://fonts.googleapis.com/css2?family=Roboto:wght@400;700&family=Roboto+Condensed:ital,wght@0,300;0,400;0,700;1,300&display=swap" rel="stylesheet">
<style>
  :root {
    --navy: #1f3a93;
    --green: #4bb543;
    --orange: #f7a83b;
    --cream: #fdfbee;
    --ink: #1d1d1d;
    --stage: #ececec;
    --white: #ffffff;
  }
  * { box-sizing: border-box; margin: 0; padding: 0; }
  html, body {
    width: 1200px; height: 814px; overflow: hidden;
    background: var(--stage);
  }
  .spread {
    position: absolute; left: 288px; top: 64px;
    display: flex; gap: 26px;
  }
  .panel {
    position: relative; width: 299px; height: 686px; overflow: hidden;
    box-shadow: 0 1px 4px rgba(0,0,0,.18);
  }

  /* Front cover */
  .cover { background: var(--white); }
  .cover__photo {
    position: absolute; left: 0; top: 0; width: 100%; height: 520px;
    background:
      linear-gradient(180deg, rgba(255,255,255,.96) 0%, rgba(255,255,255,.9) 28%, rgba(255,255,255,0) 48%),
      radial-gradient(ellipse at 35% 78%, #b26f4f 0%, #8a5a4a 22%, rgba(138,90,74,0) 48%),
      radial-gradient(ellipse at 72% 62%, #a88fa8 0%, rgba(168,143,168,0) 45%),
      linear-gradient(180deg, #e6edf3 0%, #d7dde4 60%, #b9a8a0 100%);
  }
  .cover__brand {
    position: absolute; left: 24px; top: 30px;
    font-family: "Roboto", sans-serif; font-weight: 700;
    font-size: 21px; letter-spacing: .5px; color: var(--navy);
    display: flex; align-items: center; gap: 8px;
  }
  .cover__brand-dot {
    width: 10px; height: 10px; border-radius: 50%; background: var(--orange);
  }
  .cover__title {
    position: absolute; left: 24px; top: 110px;
    font-family: "Roboto Condensed", sans-serif; font-weight: 700;
    font-size: 31px; line-height: 1.12; text-transform: uppercase;
  }
  .cover__title-line1 { color: var(--navy); display: block; }
  .cover__title-accent { color: var(--orange); }
  .cover__title-rest { color: var(--green); }
  .cover__band { position: absolute; left: 0; bottom: 0; width: 299px; height: 216px; }
  .cover__intro {
    position: absolute; left: 12px; right: 14px; top: 555px;
    font-family: "Roboto", sans-serif; font-size: 17.5px; line-height: 1.35;
    color: var(--white); letter-spacing: .2px;
  }

  /* Page 2 */
  .identifiers {
    background: var(--cream); font-family: "Roboto Condensed", sans-serif; color: var(--ink);
    display: flex; flex-direction: column;
  }
  .identifiers__head { background: var(--navy); padding: 14px 11px 4px; color: var(--white); }
  .identifiers__title {
    font-weight: 700; font-size: 24.5px; line-height: 1.1; letter-spacing: -.3px; white-space: nowrap;
  }
  .identifiers__subtitle { font-weight: 400; font-size: 20px; line-height: 1.2; margin: 2px 0 5px; }
  .identifiers__text { font-weight: 300; font-size: 11.2px; line-height: 1.3; margin-bottom: 10px; }
  .identifiers__text:last-child { margin-bottom: 0; }
  .identifiers__wave { display: block; width: 299px; height: 46px; flex: none; }
  .identifiers__body { padding: 10px 11px 0; }
  .section-title { font-weight: 400; font-size: 19px; line-height: 1.2; margin-bottom: 3px; }
  .section-text { font-weight: 300; font-size: 11.2px; line-height: 1.3; }
  .code-list { list-style: none; margin: 5px 0 7px; }
  .code-list li {
    display: flex; align-items: center; gap: 7px;
    font-weight: 300; font-size: 11.4px; line-height: 16.5px;
  }
  .tick { width: 13px; height: 11px; flex: none; }
  .section-text--note { font-style: italic; margin-top: 3px; }
</style>
</head>
<body>
<main class="spread">

  <section class="panel cover">
    <div class="cover__photo" role="img" aria-label="Photo of a smiling teenage girl resting her chin on her hands with her parents behind her"></div>
    <div class="cover__brand"><span class="cover__brand-dot"></span>City of Quellmont</div>
    <h1 class="cover__title">
      <span class="cover__title-line1">Home Roadmap</span>
      <span class="cover__title-accent">For Street</span> <span class="cover__title-rest">Safety</span>
    </h1>
    <svg class="cover__band" viewBox="0 0 299 216" preserveAspectRatio="none" aria-hidden="true">
      <path d="M0 40 C90 24 200 14 299 0 L299 216 L0 216 Z" fill="var(--green)"/>
      <path d="M0 70 C100 66 200 58 299 54 L299 216 L0 216 Z" fill="var(--orange)"/>
      <path d="M0 76 C100 72 200 66 299 60 L299 216 L0 216 Z" fill="var(--navy)"/>
    </svg>
    <p class="cover__intro">This guide is designed to provide parents with information in order to recognize and prevent gang involvement.</p>
  </section>

  <section class="panel identifiers">
    <div class="identifiers__head">
      <h2 class="identifiers__title">COMMON GANG IDENTIFIERS</h2>
      <h3 class="identifiers__subtitle">Gang-style clothing and dress</h3>
      <p class="identifiers__text">Gang members may use a particular style of dress to identify with a particular gang, set, clique, or crew. This might include clothing or bandanas worn only in certain colors that are representative of a gang.</p>
      <p class="identifiers__text">Other clothing that might be worn by gang members could include pants worn well below the waist (sagging); gang-themed T-shirts with pictures of gang members, prison scenes, graffiti, or slogans; sports clothing of specific teams; or colored fabric belts, occasionally with a metal buckle that includes the initial(s) of the gang.</p>
    </div>
    <svg class="identifiers__wave" viewBox="0 0 299 46" preserveAspectRatio="none" aria-hidden="true">
      <path d="M0 0 H299 V14 C200 16 80 30 0 46 Z" fill="var(--green)"/>
      <path d="M0 0 H299 V0 C200 4 80 14 0 28 Z" fill="var(--navy)"/>
    </svg>
    <div class="identifiers__body">
      <h3 class="section-title">Symbols and numbers</h3>
      <p class="section-text">Symbols and numbers have special significance within the gang culture. In the Quellmont area letters and symbols that contain QT, X13, or XIII indicate gang involvement. The below symbols are examples:</p>
      <ul class="code-list">
        <li><svg class="tick" viewBox="0 0 13 11"><path d="M1 6 L5 10 L12 1" fill="none" stroke="var(--green)" stroke-width="2"/></svg>X13, XIII, Sur “M”</li>
        <li><svg class="tick" viewBox="0 0 13 11"><path d="M1 6 L5 10 L12 1" fill="none" stroke="var(--green)" stroke-width="2"/></svg>QTV, QTL, QT, EQ</li>
        <li><svg class="tick" viewBox="0 0 13 11"><path d="M1 6 L5 10 L12 1" fill="none" stroke="var(--green)" stroke-width="2"/></svg>NW, NWQT, NWQT13</li>
        <li><svg class="tick" viewBox="0 0 13 11"><path d="M1 6 L5 10 L12 1" fill="none" stroke="var(--green)" stroke-width="2"/></svg>SQ, SQQT</li>
        <li><svg class="tick" viewBox="0 0 13 11"><path d="M1 6 L5 10 L12 1" fill="none" stroke="var(--green)" stroke-width="2"/></svg>MESA, MF, WSMF, MFXQT, Ridge St</li>
        <li><svg class="tick" viewBox="0 0 13 11"><path d="M1 6 L5 10 L12 1" fill="none" stroke="var(--green)" stroke-width="2"/></svg>Pikes, PKQT</li>
        <li><svg class="tick" viewBox="0 0 13 11"><path d="M1 6 L5 10 L12 1" fill="none" stroke="var(--green)" stroke-width="2"/></svg>RV, WRVST</li>
        <li><svg class="tick" viewBox="0 0 13 11"><path d="M1 6 L5 10 L12 1" fill="none" stroke="var(--green)" stroke-width="2"/></svg>BTXQT, VBT, BXT, BT</li>
      </ul>
      <h3 class="section-title">Hand signs</h3>
      <p class="section-text">Some gangs use specific hand gestures to communicate their affiliation with the gang and issue threats or challenges to rival gangs. These gestures usually include trying to shape the fingers into the letters representative of the gang.</p>
      <p class="section-text section-text--note">Gang clothing trends change so clothing alone may not be enough to indicate a child’s affiliation with a particular gang, though it can be a clue. For current information on clothing and other gang identifiers, call a gang investigator at 555-0148.</p>
    </div>
  </section>

</main>
</body>
</html>
```